Election features for a political website

The Evening Lantern (www.eveninglantern.co.uk)
Web banner designs
Please have a look at The Evening Lantern website (www.eveninglantern.co.uk). We are seeking to add an advertising style banner at the top of every page and post. It will run right across the page (1024 pixels) and be in the region of 200 pixels vertically. (Please advise on what looks best size wise.
The banner will be a slider, operated in a similar way to the current homepage slider. There will be four items on the slider, and so we need four designs that match the aesthetic feel of the website. Each slider will link through to posts on the website.
1.
Headline: OUR CANDIDATE OF THE DAY
Space for a name, head and shoulders picture of the person to be dropped in and a one line reason. This will need to be in an editable format as this image will be changed each day for one month.
2.
Headline: HERO OF THE DAY
Space for name and a one line reason. This will need to be in an editable format as this image will be changed each day for one month.
3.
Headline: VILLAIN OF THE DAY
Space for name of the person to be dropped in and a one line reason. This will need to be in an editable format as this image will be changed each day for one month.
4.
Headline: TEL Poll – [Date]
If the election was today, who would you vote for?
Clickable options:
Harbourites
Meridan
Tallow Assembly
Pomo
Quill
Other
Can a poll widget be added to the banner? We would like this poll to reset each day and then pool the results into a graph day by day over a one month period.
Reason: Payment is now guaranteed. We would like to see more options.

```html
<!DOCTYPE html>
<html lang="en">
<head>
<meta charset="utf-8">
<title>The Evening Lantern – Hero of the Day Banner</title>
<link rel="stylesheet" href="https://fonts.googleapis.com/css2?family=Open+Sans:wght@300;400;700&display=swap">
<style>
  :root {
    --page-bg: #1c1c1c;
    --sky-light: #f4f9fb;
    --sky-mid: #d6e9f1;
    --sky-edge: #a9cfe0;
    --brand-blue: #1f6fb2;
    --brand-blue-dark: #195f9c;
    --chevron-strong: #2a7cc4;
    --ribbon-light: #ffc21a;
    --ribbon-dark: #f7890f;
    --ribbon-text: #ffffff;
    --slot-top: #bcd9e8;
    --slot-bottom: #8fbfd8;
  }
  html, body {
    margin: 0;
    padding: 0;
    width: 1200px;
    height: 729px;
    overflow: hidden;
    background: var(--page-bg);
    font-family: "Open Sans", Arial, sans-serif;
  }
  .hero-banner {
    position: absolute;
    left: 90px;
    top: 177px;
    width: 1024px;
    height: 348px;
    overflow: hidden;
    background:
      radial-gradient(ellipse 60% 70% at 40% 35%, var(--sky-light) 0%, rgba(244,249,251,0) 70%),
      radial-gradient(ellipse 45% 60% at 90% 85%, var(--sky-edge) 0%, rgba(169,207,224,0) 70%),
      radial-gradient(ellipse 40% 60% at 5% 90%, var(--sky-edge) 0%, rgba(169,207,224,0) 70%),
      var(--sky-mid);
  }
  .headline {
    position: absolute;
    left: 102px;
    top: 114px;
    margin: 0;
    color: var(--brand-blue);
    font-weight: 300;
    line-height: 1;
    letter-spacing: -1.5px;
  }
  .headline-line {
    display: block;
    white-space: nowrap;
  }
  .headline-top { font-size: 52px; }
  .headline-top strong {
    font-weight: 700;
    font-size: 60px;
    color: var(--brand-blue-dark);
    letter-spacing: -2.5px;
    margin-left: 4px;
  }
  .headline-bottom { margin-top: -6px; padding-left: 71px; }
  .headline-small { font-size: 31px; letter-spacing: -1px; }
  .headline-day { font-size: 54px; }
  .chevrons {
    position: absolute;
    left: 347px;
    top: 133px;
    width: 130px;
    height: 86px;
  }
  .profile {
    position: absolute;
    left: 588px;
    top: 43px;
    width: 312px;
    text-align: center;
  }
  .portrait-slot {
    width: 175px;
    height: 172px;
    margin: 0 auto;
    border-radius: 4px;
    background: linear-gradient(180deg, var(--slot-top) 0%, var(--slot-bottom) 100%);
  }
  .name-ribbon {
    position: relative;
    width: 256px;
    height: 38px;
    margin: -1px auto 0;
  }
  .name-ribbon svg { position: absolute; inset: 0; width: 100%; height: 100%; }
  .name-ribbon span {
    position: relative;
    display: block;
    line-height: 38px;
    color: var(--ribbon-text);
    font-weight: 700;
    font-size: 17px;
    letter-spacing: -0.3px;
  }
  .reason {
    margin: 5px 0 0;
    color: var(--brand-blue);
    font-size: 13px;
    letter-spacing: -0.4px;
    white-space: nowrap;
  }
</style>
</head>
<body>
  <section class="hero-banner">
    <h1 class="headline">
      <span class="headline-line headline-top">Our<strong>Hero</strong></span>
      <span class="headline-line headline-bottom"><span class="headline-small">of the</span> <span class="headline-day">Day</span></span>
    </h1>

    <svg class="chevrons" viewBox="0 0 130 86" aria-hidden="true">
      <defs>
        <linearGradient id="chevron-fade" x1="0" x2="1" y1="0" y2="0">
          <stop offset="0" stop-color="#ffffff" stop-opacity=".3"/>
          <stop offset="1" stop-color="#2a7cc4"/>
        </linearGradient>
      </defs>
      <g fill="url(#chevron-fade)">
        <polygon points="0,0 16,0 34,43 16,86 0,86 18,43"/>
        <polygon points="24,0 40,0 58,43 40,86 24,86 42,43"/>
        <polygon points="48,0 64,0 82,43 64,86 48,86 66,43"/>
        <polygon points="72,0 88,0 106,43 88,86 72,86 90,43"/>
      </g>
      <polygon fill="var(--chevron-strong)" points="96,0 112,0 130,43 112,86 96,86 114,43"/>
    </svg>

    <div class="profile">
      <div class="portrait-slot" role="img" aria-label="Head and shoulders portrait of the day's hero"></div>
      <div class="name-ribbon">
        <svg viewBox="0 0 256 38" preserveAspectRatio="none" aria-hidden="true">
          <defs>
            <linearGradient id="ribbon-fill" x1="0" x2="0" y1="0" y2="1">
              <stop offset="0" stop-color="var(--ribbon-light)"/>
              <stop offset="1" stop-color="var(--ribbon-dark)"/>
            </linearGradient>
          </defs>
          <polygon fill="url(#ribbon-fill)" points="0,0 256,0 238,19 256,38 0,38 18,19"/>
        </svg>
        <span>John Doe</span>
      </div>
      <p class="reason">This will need to be in an editable format as this image</p>
    </div>
  </section>
</body>
</html>
```